WooCommerce Web Design for SEO Agency

Looking for a clean and fast WooCommerce design

Selling 5 different products each with maybe 3-4 variants

Need imagery - featured images, basic logo etc

I will supply all content and most is ready to go (or can be in a few days)

You will need to design and build the site including some basic WooCommerce configuration - PayPal, checkout forms etc

Target Market(s)

SEO, Internet marketers

Coding

Coded - Design and coding required

Number of Pages Required

3 page

Font styles to use
Sans Serif

Requirements
Must have
• WooCommerce and WP integration

```html
<!DOCTYPE html>
<html lang="en">
<head>
<meta charset="utf-8">
<title>Marcus Lowell – Digital Due Diligence</title>
<link href="https://fonts.googleapis.com/css2?family=Poppins:wght@300;400;500;600;700&display=swap" rel="stylesheet">
<style>
:root{
  --blue:#1565a8;
  --blue-text:#1a5f9f;
  --blue-dark:#0f4f8b;
  --hero-a:#5a4a44;
  --hero-b:#c9674a;
  --ink:#3d3d3d;
  --muted:#6b6b6b;
  --grey-bg:#e9e9e9;
  --card-bg:#f1f1f1;
  --footer-bg:#262626;
  --white:#ffffff;
}
*{box-sizing:border-box;margin:0;padding:0}
html,body{width:1200px;height:5199px;overflow:hidden}
body{font-family:'Poppins',sans-serif;color:var(--ink);background:var(--white);position:relative}
.abs{position:absolute}
/* hero */
.hero{position:absolute;left:0;top:0;width:1200px;height:760px}
.hero-photo{position:absolute;inset:0;background:linear-gradient(135deg,#3b3532 0%,var(--hero-a) 35%,var(--hero-b) 70%,#e9a98b 100%);clip-path:polygon(0 0,100% 0,100% 615px,50% 760px,0 615px)}
.hero-shade{position:absolute;inset:0;background:rgba(0,0,0,.18);clip-path:polygon(0 0,100% 0,100% 615px,50% 760px,0 615px)}
.brand{position:absolute;left:143px;top:18px;display:flex;align-items:center;gap:10px;color:var(--white)}
.brand-mark{width:44px;height:44px;border:2px solid var(--white)}
.brand-name{font-size:26px;font-weight:600;letter-spacing:1px;line-height:1}
.brand-sub{font-size:11px;letter-spacing:3.5px;margin-top:4px}
.nav{position:absolute;left:486px;top:30px;display:flex;gap:28px;font-size:11px;color:var(--white);font-weight:500}
.nav .active{color:#7fbcf0}
.nav-icons{position:absolute;left:955px;top:26px;display:flex;gap:22px}
.hero-title{position:absolute;right:145px;top:262px;text-align:right;color:var(--white);font-size:47px;font-weight:700;line-height:52px;letter-spacing:-.5px}
.btn{display:inline-block;background:var(--blue);color:var(--white);font-size:15px;font-weight:500;text-align:center}
.hero-btn{position:absolute;left:893px;top:378px;width:160px;height:46px;line-height:46px;font-size:17px;font-weight:600}
.arrow{position:absolute}
/* intro */
.intro{position:absolute;top:830px;left:0;width:1200px;text-align:center}
.intro h2{color:var(--blue-text);font-size:32px;font-weight:600;line-height:52px}
.intro p{font-size:14.5px;line-height:35px;color:var(--ink);margin-top:12px}
.intro .btn{margin-top:16px;width:128px;height:44px;line-height:44px}
/* services */
.services{position:absolute;top:1301px;left:0;width:1200px;height:399px;display:flex;gap:3px}
.service{flex:1;position:relative;display:flex;align-items:flex-end;justify-content:center;padding-bottom:38px}
.service h3{color:var(--white);font-size:24px;font-weight:500;text-align:center;line-height:36px;position:relative}
.svc1{background:linear-gradient(160deg,#c9c2b8,#6f6760 60%,#3a3532)}
.svc2{background:linear-gradient(160deg,#e3e0dc,#9a928b 55%,#4a4440)}
.svc3{background:linear-gradient(160deg,#d7d8da,#8a8d92 55%,#3d3f43)}
/* products */
.products{position:absolute;top:1770px;left:0;width:1200px;text-align:center}
.section-title{color:var(--blue-text);font-size:32px;font-weight:600}
.product-row{position:absolute;left:143px;top:61px;display:flex;gap:9px}
.product{width:176px;height:175px;background:var(--blue);color:var(--white);display:flex;flex-direction:column;align-items:center;padding-top:30px;font-size:15px;line-height:24px}
.product svg{margin-bottom:18px}
/* about */
.about-photo{position:absolute;left:0;top:2086px;width:600px;height:599px;background:linear-gradient(120deg,#e8ebee,#b7c0c9 45%,#2d3a55 75%,#d6d9dd)}
.about-panel{position:absolute;left:600px;top:2118px;width:600px;height:601px;background:var(--blue);color:var(--white);padding:98px 140px 0 48px}
.about-panel h3{font-size:20px;font-weight:600;line-height:32px}
.about-panel p{font-size:12px;line-height:26px;margin-top:20px;color:#dbe8f5}
.about-panel .btn-outline{display:inline-block;margin-top:30px;background:var(--white);color:var(--blue);width:129px;height:45px;line-height:45px;text-align:center;font-size:15px}
/* testimonials */
.testimonials{position:absolute;top:2785px;left:0;width:1200px;text-align:center}
.testimonials .lead{font-size:15px;line-height:30px;margin:14px auto 0;width:910px}
.quotes{position:absolute;left:143px;top:156px;display:flex;gap:10px}
.quote{width:298px;height:417px;background:var(--card-bg);position:relative}
.quote.mid{background:#e4e4e4}
.quote p{font-size:13.5px;line-height:32px;padding:56px 28px 0;color:var(--muted)}
.quote svg.q{display:block;margin:22px auto 0}
.quote-foot{position:absolute;left:0;bottom:0;width:100%;height:66px;background:var(--blue);color:var(--white);padding-top:12px}
.quote-foot::before{content:"";position:absolute;left:50%;top:-10px;margin-left:-11px;border-left:11px solid transparent;border-right:11px solid transparent;border-bottom:10px solid var(--blue)}
.quote-foot strong{display:block;font-size:15px;font-weight:600}
.quote-foot span{font-size:10px;color:#cfe0f1}
/* cta */
.cta-top{position:absolute;left:0;top:3469px;width:600px;height:303px;background:var(--blue);color:var(--white);padding:68px 40px 0 143px;font-size:20px;font-weight:600;line-height:32px}
.cta-bottom{position:absolute;left:0;top:3772px;width:600px;height:297px;background:var(--blue-dark);color:#dbe8f5;padding:38px 40px 0 143px;font-size:15px;line-height:35px}
.cta-bottom .sig{margin-top:14px;color:var(--white);font-size:18px}
.cta-photo{position:absolute;left:600px;top:3439px;width:600px;height:599px;background:linear-gradient(130deg,#eef0f2,#c9cdd1 45%,#8a8581 70%,#e0e1e2)}
/* companies */
.companies{position:absolute;top:4140px;left:0;width:1200px;text-align:center}
.companies .lead{font-size:15px;line-height:30px;margin:14px auto 0;width:910px}
.partners{position:absolute;top:162px;left:0;width:1200px;display:flex;justify-content:space-around;padding:0 200px}
.partner{font-size:22px;font-weight:700;color:#3a3a3a;display:flex;align-items:center;gap:8px}
.partner .dot{width:12px;height:12px;border-radius:50%;background:#e5502d}
/* contact */
.contact{position:absolute;top:4411px;left:0;width:1200px;height:456px;background:var(--grey-bg);text-align:center}
.contact .section-title{margin-top:70px}
.fields{position:absolute;left:143px;top:131px;display:flex;gap:14px}
.field{width:219px;height:37px;background:var(--white);border:1px solid #cfcfcf;font-size:11px;color:#555;text-align:left;padding:11px 16px}
.message{position:absolute;left:143px;top:188px;width:912px;height:117px;background:var(--white);border:1px solid #cfcfcf;font-size:11px;color:#555;text-align:left;padding:12px 16px}
.contact .btn{position:absolute;left:551px;top:327px;width:96px;height:47px;line-height:47px}
/* footer */
.footer{position:absolute;top:4867px;left:0;width:1200px;height:332px;background:var(--footer-bg);color:#bdbdbd;font-size:11px}
.footer h4{color:var(--white);font-size:15px;font-weight:500;margin-bottom:14px}
.fcol{position:absolute;top:42px}
.fcol li{list-style:none;line-height:27px}
.info-row{display:flex;gap:14px;line-height:18px;margin-bottom:22px}
.social{display:flex;gap:16px}
.social span{width:48px;height:48px;border:1px solid #8a8a8a;border-radius:50%;display:flex;align-items:center;justify-content:center;color:var(--white);font-size:13px}
.news-form{display:flex;margin-top:14px}
.news-form .in{width:168px;height:42px;background:#d9d9d9;color:#444;padding:14px 16px;font-size:10px}
.news-form .btn{width:112px;height:42px;line-height:42px;font-size:15px}
.copyright{position:absolute;top:290px;left:0;width:1200px;text-align:center;font-size:10px;color:#a8a8a8}
</style>
</head>
<body>

<header class="hero">
  <div class="hero-photo" role="img" aria-label="Laptop on a desk showing a search marketing website"></div>
  <div class="hero-shade"></div>
  <div class="brand">
    <div class="brand-mark"></div>
    <div>
      <div class="brand-name">MARCUS LOWELL</div>
      <div class="brand-sub">DIGITAL DUE DILIGENCE</div>
    </div>
  </div>
  <nav class="nav">
    <span class="active">HOME</span><span>ABOUT US</span><span>SERVICES</span><span>PRODUCTS</span><span>REVIEWS</span><span>CONTACT US</span>
  </nav>
  <div class="nav-icons">
    <svg width="16" height="16" viewBox="0 0 16 16"><circle cx="6.5" cy="6.5" r="5" fill="none" stroke="#fff" stroke-width="2"/><line x1="10" y1="10" x2="15" y2="15" stroke="#fff" stroke-width="2.4"/></svg>
    <svg width="16" height="16" viewBox="0 0 16 16"><circle cx="8" cy="5" r="4" fill="#fff"/><path d="M1 16c0-5 14-5 14 0z" fill="#fff"/></svg>
    <svg width="18" height="16" viewBox="0 0 18 16"><path d="M0 1h3l2 9h10l2-7H5" fill="none" stroke="#fff" stroke-width="2"/><circle cx="7" cy="14" r="1.6" fill="#fff"/><circle cx="14" cy="14" r="1.6" fill="#fff"/></svg>
  </div>
  <h1 class="hero-title">DUE DILIGENCE FOR<br>YOUR DIGITAL ASSETS.</h1>
  <span class="btn hero-btn">GET IN TOUCH</span>
  <svg class="arrow" style="left:54px;top:328px" width="18" height="30" viewBox="0 0 18 30"><polyline points="15,2 3,15 15,28" fill="none" stroke="#fff" stroke-width="4"/></svg>
  <svg class="arrow" style="left:1126px;top:328px" width="18" height="30" viewBox="0 0 18 30"><polyline points="3,2 15,15 3,28" fill="none" stroke="#fff" stroke-width="4"/></svg>
</header>

<section class="intro">
  <h2>I am neither a lawyer nor an accountant.<br>I am a commercial digital marketer.</h2>
  <p>I have learnt a lot since I made my first $$ online in 2005. I have made millions and lost thousands. I have been in<br>
  many situations you may find yourself in today and now I want to work with you to make you fly further, faster.<br>
  I am an internationally respected SEO speaker, educator, and digital business leader.<br>
  I have an eye for detail and a unique skill set that enables the traits needed to excel at Digital Due Diligence.<br>
  Combined with a love for scaling websites via digital marketing strategies and tactics,<br>
  you can see why I can be the most valuable weapon in your arsenal.</p>
  <span class="btn">READ MORE</span>
</section>

<section class="services">
  <div class="service svc1" role="img" aria-label="Hands at a desk with a phone and tablet"><h3>Digital Due Diligence</h3></div>
  <div class="service svc2" role="img" aria-label="Hands typing on a laptop keyboard"><h3>New Agency Selection<br>Support</h3></div>
  <div class="service svc3" role="img" aria-label="Printed charts and a laptop on a desk"><h3>Existing Agency Auditing<br>Service</h3></div>
</section>

<section class="products">
  <h2 class="section-title">Products</h2>
  <div class="product-row">
    <div class="product"><svg width="46" height="52" viewBox="0 0 46 52" fill="none" stroke="#fff" stroke-width="2"><rect x="8" y="2" width="30" height="44"/><line x1="14" y1="12" x2="32" y2="12"/><line x1="14" y1="20" x2="32" y2="20"/><line x1="14" y1="28" x2="32" y2="28"/><line x1="14" y1="36" x2="26" y2="36"/></svg>Suspendisse<br>elit ligula</div>
    <div class="product"><svg width="52" height="52" viewBox="0 0 52 52" fill="none" stroke="#fff" stroke-width="2"><circle cx="22" cy="22" r="14"/><line x1="32" y1="32" x2="48" y2="48"/><polyline points="14,26 20,18 26,24 30,16"/></svg>Phasellus blandit<br>quam</div>
    <div class="product"><svg width="52" height="52" viewBox="0 0 52 52" fill="none" stroke="#fff" stroke-width="2"><circle cx="20" cy="20" r="10"/><circle cx="20" cy="20" r="4"/><circle cx="36" cy="36" r="9"/><circle cx="36" cy="36" r="3"/></svg>Fusce porta<br>arcu mi</div>
    <div class="product"><svg width="56" height="52" viewBox="0 0 56 52" fill="none" stroke="#fff" stroke-width="2"><rect x="4" y="4" width="48" height="32"/><line x1="20" y1="46" x2="36" y2="46"/><line x1="28" y1="36" x2="28" y2="46"/><rect x="12" y="14" width="10" height="14"/><rect x="26" y="12" width="18" height="8"/></svg>Cras sed augue<br>tortor</div>
    <div class="product"><svg width="52" height="52" viewBox="0 0 52 52" fill="none" stroke="#fff" stroke-width="2"><rect x="6" y="34" width="6" height="14"/><rect x="18" y="28" width="6" height="20"/><rect x="30" y="22" width="6" height="26"/><rect x="42" y="14" width="6" height="34"/><polyline points="6,22 18,14 30,16 44,4"/></svg>Praesent<br>accumsan nunc</div>
  </div>
</section>

<div class="about-photo" role="img" aria-label="Portrait of Marcus Lowell seated in front of a marketing wall mural"></div>
<section class="about-panel">
  <h3>Why choose me for your digital due<br>diligence or agency auditing?</h3>
  <p>My name, Marcus Lowell, is synonymous with SEO and digital marketing expertise.</p>
  <p>I am a leading industry expert and respected speaker, educating the brightest minds in digital business on my trusted and cutting edge methods of planning and implementing digital techniques that get results.</p>
  <p>Please see the About Me page for further information on my business credentials.</p>
  <span class="btn-outline">ABOUT ME</span>
</section>

<section class="testimonials">
  <h2 class="section-title">All sounds great. What do your clients say?</h2>
  <p class="lead">Testimonials capture the attention. They show what's gone before. They promise what's to come. What I want you to focus on is that testimonials like these could soon be on your site. Sound good? Fill in the form and let's do this.</p>
  <svg class="arrow" style="left:54px;top:283px" width="14" height="24" viewBox="0 0 14 24"><polyline points="12,2 2,12 12,22" fill="none" stroke="#777" stroke-width="3"/></svg>
  <svg class="arrow" style="left:1130px;top:283px" width="14" height="24" viewBox="0 0 14 24"><polyline points="2,2 12,12 2,22" fill="none" stroke="#777" stroke-width="3"/></svg>
  <div class="quotes">
    <div class="quote">
      <svg class="q" width="32" height="26" viewBox="0 0 32 26"><path d="M0 12C0 4 5 0 12 0v5c-4 0-6 3-6 7h6v14H0zM18 12c0-8 5-12 12-12v5c-4 0-6 3-6 7h6v14H18z" fill="#555"/></svg>
      <p style="padding-top:18px">Grateful for the opportunity to train under Marcus's direction. A 217% increase in lead generation (business IT supplies) during the following quarter. The future is looking bright thanks to the advice and guidance Marcus provides.</p>
      <div class="quote-foot"><strong>CEO</strong><span>Hong Kong based Exporter</span></div>
    </div>
    <div class="quote mid">
      <svg class="q" width="32" height="26" viewBox="0 0 32 26"><path d="M0 12C0 4 5 0 12 0v5c-4 0-6 3-6 7h6v14H0zM18 12c0-8 5-12 12-12v5c-4 0-6 3-6 7h6v14H18z" fill="#555"/></svg>
      <p style="padding-top:18px">We were sceptical at first. A new website with page 1 search ranking, a new targeted pitch strategy, and a dedicated online client interaction facility later, and we finally understand. Our most grateful thanks.</p>
      <div class="quote-foot"><strong>CMO</strong><span>US Real Estate Conglomerate</span></div>
    </div>
    <div class="quote">
      <svg class="q" width="32" height="26" viewBox="0 0 32 26"><path d="M0 12C0 4 5 0 12 0v5c-4 0-6 3-6 7h6v14H0zM18 12c0-8 5-12 12-12v5c-4 0-6 3-6 7h6v14H18z" fill="#555"/></svg>
      <p style="padding-top:18px">We approached Marcus Lowell for marketing agency pitch support. The problem wasn't the agencies – our brand message was strong but perhaps too diverse. Marcus gave us a niche online presence. A lesson learned.</p>
      <div class="quote-foot"><strong>Head of Digital Services</strong><span>Top UK Based Fashion Company</span></div>
    </div>
  </div>
</section>

<div class="cta-photo" role="img" aria-label="Marcus Lowell in a white polo shirt in front of a marketing wall mural"></div>
<section class="cta-top">Your initial consultation with me is FREE Discover how my SEO guidance, commercial marketing skill set and Digital Due Diligence processes can help you to realise the full potential of your business.</section>
<section class="cta-bottom">
  <p>"Websites are valuable assets. Organic search visibility can rocket your valuations or bring you to your knees in tears. My job is to make sure you do the right things, buy the right things, and measure the right things."</p>
  <p class="sig">– Marcus Lowell.</p>
</section>

<section class="companies">
  <h2 class="section-title">Companies I Have Worked With</h2>
  <p class="lead">With over 15 years of experience in training the most forward thinking business leaders in their niche, I'm proud to say thank you for the opportunity to have worked with the best.</p>
  <div class="partners">
    <div class="partner"><span class="dot"></span>Rankwise</div>
    <div class="partner">Travelora</div>
    <div class="partner">Kestrel Capital</div>
  </div>
</section>

<section class="contact">
  <h2 class="section-title">Contact us</h2>
  <div class="fields">
    <div class="field">Name</div><div class="field">Email</div><div class="field">Company</div><div class="field">Subject</div>
  </div>
  <div class="message">Message</div>
  <span class="btn">SUBMIT</span>
</section>

<footer class="footer">
  <div class="fcol" style="left:143px;width:260px">
    <h4>Contact Info</h4>
    <div class="info-row"><svg width="10" height="14" viewBox="0 0 10 14"><path d="M5 0a5 5 0 0 1 5 5c0 4-5 9-5 9S0 9 0 5a5 5 0 0 1 5-5z" fill="#bdbdbd"/><circle cx="5" cy="5" r="2" fill="#262626"/></svg><span>Marcus Lowell<br>3rd Floor, Alder House, Mill Lane<br>Northfield, Eastshire, NF2 4QT<br>United Kingdom</span></div>
    <div class="info-row"><svg width="12" height="12" viewBox="0 0 12 12"><path d="M2 0l3 3-1.5 2c1 2 2 3 3.5 3.5L9 7l3 3-2 2C5 12 0 7 0 2z" fill="#bdbdbd"/></svg><span>0100 555 0142</span></div>
    <div class="info-row"><svg width="13" height="10" viewBox="0 0 13 10"><rect width="13" height="10" fill="#bdbdbd"/><polyline points="0,0 6.5,6 13,0" fill="none" stroke="#262626" stroke-width="1.2"/></svg><span>hello@marcuslowell.example</span></div>
  </div>
  <div class="fcol" style="left:447px">
    <h4>Links</h4>
    <ul><li>Home</li><li>About Us</li><li>Services</li><li>Products</li><li>Reviews</li><li>Contact Us</li></ul>
  </div>
  <div class="fcol" style="left:583px">
    <h4>Follow us on</h4>
    <div class="social"><span>S1</span><span>S2</span></div>
  </div>
  <div class="fcol" style="left:772px">
    <h4>Newsletter SignUp</h4>
    <div>Mauris pulvinar volutpat ipsum, nec sodales dignissim</div>
    <div class="news-form"><div class="in">Email Address</div><span class="btn">SUBSCRIBE</span></div>
  </div>
  <div class="copyright">Copyright © 2020 Marcus Lowell. All rights reserved.</div>
</footer>

</body>
</html>
```